AMBER AND STONE WEB

We need a home design in wordpress, we have now a web but we would like to improve it. Our current web is www.amberandstonevillas.example Our business is holliday rental of villas in Ibiza. Our guest must know that we are a reliable company, professional and with experience and good reviews. We want them to click in our reservation engine: https://bookings.amberandstonevillas.example/en/ and make reservation in our website. We would also like to say that all the properties that we have are just us who commercialize so we have best price available. Many people are going to see our villas in staylister.example and look to our website to make a reservation with us so we need to show them that they are at the right place and click at our link to our reservation engine. What make us special is that we are a local company, we are from Ibiza, Our guests are always received in person by the Amber and Stone Villas team. You will enjoy extensive tourist information when you check in and during the entire stay. You will be attended by ChatLoop and calls, always happy to help so that you have a happy and fun stay! Our guest stay is better than in hotel as they have more spece, private swiming pool, private garden, barbeque ... To rent a villa is the best way to stay in Ibiza. We also have a promotional video: https://vidshare.example/Qm7tLp2Xz9A Let our philosophy be shown, we think that coming on holiday to Ibiza implies seeing the nature that we have in Ibiza, hence our name AMBER AND STONE, like the pins that almost touch the sea in Ibiza, or the posidonea meadows where the intense green of the seaweed and the blue of the sea. We are aware of the environment, and we love Ibiza. For us, the client who visits Ibiza, should rent a car, go around the island, eat in a restaurant one day in front of the sea, is a night of partying to the discs, go shopping, visit the ancient heritage of Umanity, make some aquatic sport, enjoy the pool, those are for us Ibiza.

Target Market(s)

Europe, people from Holand, UK, Germany, France, Spain ...

Industry/Entity Type

Tourism

Colors

Designer to choose colors to be used in the design.

Requirements
Must have
• Pictures of Ibiza.
Nice to have
• Our name Amber and Stone Villas is beacuse in Ibiza there is forest that almost touch the watter of the Mediterranean sea, so you can see green of the forest and blue of the sea and the sky. And also beacause under the watter of the sea there is a plant called Posidonia that is also green please see the picture of posidonia.

```html
<!DOCTYPE html>
<html lang="en">
<head>
<meta charset="utf-8">
<title>Amber and Stone Villas Ibiza — Home</title>
<link href="https://fonts.googleapis.com/css2?family=Cinzel:wght@400;600;700&family=Poppins:ital,wght@0,300;0,400;0,500;0,600;1,300;1,400&display=swap" rel="stylesheet">
<style>
:root{
  --green:#6f9b2c;
  --green-dark:#4f7d22;
  --teal:#2a8c9c;
  --text:#3a3a3a;
  --muted:#6b6b6b;
  --line:#e3e3e3;
  --white:#ffffff;
  --heading:#5e9233;
}
*{box-sizing:border-box;margin:0;padding:0}
html,body{width:1200px;height:4335px;overflow:hidden}
body{font-family:'Poppins',sans-serif;color:var(--text);background:var(--white);position:relative}
section,header,footer{position:absolute;left:0;width:1200px}

/* header */
.site-header{top:0;height:135px;background:var(--white)}
.brand{position:absolute;left:143px;top:38px;display:flex;align-items:center;gap:12px}
.brand-dot{width:44px;height:44px;border-radius:50%;background:var(--green)}
.brand-name{font-family:'Cinzel',serif;font-size:25px;color:var(--green);font-weight:600;letter-spacing:.5px;line-height:1}
.call{position:absolute;right:218px;top:18px;display:flex;align-items:center;gap:10px;font-size:18px;color:#444}
.call b{font-weight:600;color:#222}
.call-icon{width:34px;height:34px;border-radius:50%;background:var(--green);display:flex;align-items:center;justify-content:center}
.lang{position:absolute;right:142px;top:19px;width:62px;height:30px;border:2px solid var(--teal);border-radius:16px;display:flex;align-items:center;justify-content:center;gap:8px}
.lang-flag{width:24px;height:15px;background:linear-gradient(#b22 0 14%,#fff 14% 28%,#b22 28% 42%,#fff 42% 56%,#b22 56% 70%,#fff 70% 84%,#b22 84%);position:relative}
.lang-flag:before{content:"";position:absolute;left:0;top:0;width:11px;height:8px;background:#2b3f8f}
.main-nav{position:absolute;right:142px;top:78px;display:flex;align-items:center;gap:31px;font-family:'Cinzel',serif;font-size:14px;color:#333}
.main-nav .active{color:var(--green);position:relative}
.main-nav .active:after{content:"";position:absolute;left:0;right:0;bottom:-10px;height:2px;background:var(--green)}
.btn-outline{border:2px solid var(--teal);border-radius:20px;padding:6px 14px;color:#333}

/* hero */
.hero{top:135px;height:538px;background:linear-gradient(180deg,#8fb7d6 0%,#c9d8d8 22%,#a07a5a 40%,#6c7f5a 52%,#2a9fd0 62%,#1a86c5 80%,#2b93c9 92%,#ffffff 100%)}
.hero-photo{position:absolute;inset:0}
.hero-title{position:absolute;top:150px;width:100%;text-align:center;font-family:'Cinzel',serif;font-size:44px;color:#fff;font-weight:600;letter-spacing:1px;text-shadow:0 2px 8px rgba(0,0,0,.4)}
.hero-sub{position:absolute;top:207px;width:100%;text-align:center;color:#fff;font-size:16px;text-shadow:0 1px 4px rgba(0,0,0,.5)}
.search{position:absolute;left:177px;top:242px;width:845px;height:103px;background:rgba(255,255,255,.22);border-radius:10px;padding:14px 22px}
.search-labels{display:flex;font-size:11px;color:#fff;margin-bottom:10px}
.search-row{display:flex;gap:9px;align-items:center}
.field{height:38px;background:#fff;border-radius:3px;font-size:11px;color:#777;display:flex;align-items:center;justify-content:space-between;padding:0 12px}
.btn-search{height:40px;width:155px;background:linear-gradient(90deg,var(--green),var(--teal));color:#fff;font-size:18px;font-weight:500;border-radius:3px;display:flex;align-items:center;justify-content:center;letter-spacing:.5px}
.dots{position:absolute;top:450px;width:100%;display:flex;justify-content:center;gap:9px}
.dots i{width:11px;height:11px;border-radius:50%;background:#fff}
.dots i.on{background:var(--green)}

/* section headings */
.rule{display:block;width:44px;height:3px;background:var(--green);margin:20px auto 9px;border-radius:2px}
.rule.left{margin:20px 0 9px}
.rule.light{background:#fff}
.section-title{font-family:'Cinzel',serif;font-weight:600;text-align:center;color:var(--heading);font-size:42px;letter-spacing:.5px}

/* about */
.about{top:673px;height:817px;background:linear-gradient(180deg,#ffffff 0%,#fbf9f5 40%,#eef3f1 55%,#f1dcb6 75%,#e9c99a 100%)}
.about-inner{position:absolute;top:60px;width:100%;text-align:center}
.about-sub{font-size:19px;color:#333;margin-top:2px}
.about-copy{width:860px;margin:42px auto 0;font-size:13px;line-height:27px;color:#333}
.about-copy em{font-style:normal;color:var(--green-dark)}
.about-copy p+p{margin-top:10px}
.amenities{position:absolute;top:440px;left:143px;width:914px;display:flex;justify-content:space-between}
.amenity{width:100px;text-align:center;font-size:12.5px;color:#333;line-height:15px}
.amenity-icon{width:72px;height:72px;border-radius:50%;background:#fff;border:3px solid #e8e8e8;margin:0 auto 12px;display:flex;align-items:center;justify-content:center}
.btn-pill{display:inline-flex;align-items:center;justify-content:center;background:linear-gradient(90deg,var(--green),var(--teal));color:#fff;border-radius:24px;font-size:15px;letter-spacing:.5px}
.read-more{position:absolute;top:589px;left:527px;width:148px;height:42px}

/* beaches */
.beaches{top:1490px;height:585px}
.villa-slide{position:absolute;left:141px;top:92px;width:459px;height:405px;background:linear-gradient(180deg,#5d8d3a 0%,#7fa054 30%,#2c9cd0 45%,#1b86c4 55%,#c9b89c 70%,#a89274 100%)}
.villa-name{position:absolute;left:20px;bottom:26px;color:#fff;font-size:18px;font-weight:600}
.slide-arrows{position:absolute;right:0;bottom:0;display:flex}
.slide-arrows span{width:36px;height:36px;display:flex;align-items:center;justify-content:center}
.beaches-text{position:absolute;left:636px;top:122px;width:440px}
.beaches-text h2{font-family:'Cinzel',serif;font-weight:600;font-size:38px;line-height:50px;color:var(--teal);margin-top:14px}
.beaches-text h3{font-family:'Cinzel',serif;font-weight:600;font-size:24px;color:#222;margin-top:8px;letter-spacing:.5px}
.beaches-text p{font-size:18px;line-height:29px;color:#222;margin-top:14px;font-weight:500}
.contact-today{width:218px;height:42px;margin-top:16px}

/* video banner */
.video-banner{top:2075px;height:542px;background:linear-gradient(180deg,#d4c3a9 0%,#b8926b 35%,#8a6244 60%,#4d3a2b 85%,#2c231c 100%)}
.video-banner .shade{position:absolute;inset:0;background:linear-gradient(180deg,rgba(0,0,0,0) 40%,rgba(0,0,0,.45) 100%)}
.play{position:absolute;left:565px;top:225px}
.video-title{position:absolute;top:305px;width:100%;text-align:center;font-family:'Cinzel',serif;font-size:42px;color:#fff;font-weight:600;letter-spacing:.5px}
.video-sub{position:absolute;top:362px;width:100%;text-align:center;color:#fff;font-size:26px;font-weight:600}
.watch{position:absolute;top:420px;left:509px;width:182px;height:42px}

/* gallery */
.gallery{top:2617px;height:685px}
.gallery .head{position:absolute;top:86px;width:100%}
.gallery-grid{position:absolute;top:206px;left:0;width:1200px;height:480px;display:grid;grid-template-columns:repeat(4,300px);grid-template-rows:240px 240px}
.tile{position:relative}
.t-pool{background:linear-gradient(180deg,#5a9fe0 0%,#bcd6f0 30%,#2a8fd6 55%,#1670b8 80%,#e48b3a 100%)}
.t-beach{grid-row:span 2;background:linear-gradient(180deg,#1f6d72 0%,#4a9aa0 20%,#c8b49a 50%,#d9c4a6 100%)}
.t-terrace{background:linear-gradient(180deg,#6b4a2a 0%,#8a6440 30%,#9ec4de 60%,#e8e2d4 100%)}
.t-bedroom{background:linear-gradient(180deg,#f2efe9 0%,#e7e0d4 50%,#d2c1a6 100%)}
.t-bedroom2{background:linear-gradient(180deg,#f3eee4 0%,#e0d4c2 55%,#b89367 100%)}
.t-lounge{background:linear-gradient(180deg,#f0ece4 0%,#b98a5c 45%,#5a4a54 80%,#8a6a48 100%)}
.t-garden{background:linear-gradient(180deg,#7ab3dd 0%,#5e8c3e 35%,#2e96d0 60%,#d9ccb6 100%)}
.expand{position:absolute;left:117px;top:205px;width:65px;height:65px;border:2px solid #fff;display:flex;align-items:center;justify-content:center}
.view-all{position:absolute;left:544px;top:390px;width:112px;height:112px;border-radius:50%;background:var(--green-dark);border:4px solid #fff;display:flex;align-items:center;justify-content:center;text-align:center;color:#fff;font-family:'Cinzel',serif;font-size:22px;line-height:26px;font-weight:600;z-index:2}

/* testimonials */
.testimonials{top:3302px;height:555px}
.testimonials .head{position:absolute;top:100px;width:100%}
.avatar{position:absolute;left:557px;top:222px;width:86px;height:86px;border-radius:50%;background:linear-gradient(135deg,#e9a27a,#c96a4a);border:4px solid #f1f1f1}
.quote-name{position:absolute;top:328px;width:100%;text-align:center;color:var(--green-dark);font-size:15px;font-weight:500}
.quote{position:absolute;left:258px;top:360px;width:684px;text-align:center;font-size:12.5px;line-height:23px;font-style:italic;font-weight:300;color:#333}
.qmark{position:absolute;font-family:'Cinzel',serif;font-size:48px;color:var(--green);line-height:1}
.arrow-box{position:absolute;top:334px;width:38px;height:38px;display:flex;align-items:center;justify-content:center}
.arrow-prev{left:140px;border:1px solid #ddd;background:#fff}
.arrow-next{left:1021px;background:var(--green)}
.t-dots{position:absolute;top:459px;width:100%;display:flex;justify-content:center;gap:9px}
.t-dots i{width:10px;height:10px;border-radius:50%;background:#cfcfcf}
.t-dots i.on{background:var(--green)}

/* contact */
.contact{top:3857px;height:325px;background:linear-gradient(180deg,#c9d6de 0%,#a8b9c4 35%,#7c8c86 60%,#5c6a70 100%)}
.contact .shade{position:absolute;inset:0;background:rgba(10,30,50,.45)}
.contact .head{position:absolute;top:80px;width:100%}
.contact .section-title{color:#fff}
.contact-items{position:absolute;top:198px;left:141px;width:920px;display:flex;justify-content:space-between;color:#fff}
.c-item{display:flex;gap:14px;align-items:flex-start;font-size:13px;line-height:20px}
.c-icon{width:36px;height:36px;border:2px solid #fff;border-radius:50%;flex:none;display:flex;align-items:center;justify-content:center}
.c-item .label{font-size:14px}
.c-item .val{font-size:15px;font-weight:500}

/* footer */
.site-footer{top:4182px;height:153px;background:#fff}
.site-footer .brand{top:54px}
.foot-nav{position:absolute;left:535px;top:48px;width:521px;display:flex;justify-content:space-between;font-family:'Cinzel',serif;font-size:14px;color:#333}
.copyright{position:absolute;left:528px;top:100px;font-size:11px;color:#444}
.social{position:absolute;right:142px;top:90px;display:flex;gap:8px}
.social i{width:28px;height:28px;border-radius:50%}
.social i.a{background:#2d3f8e}
.social i.b{background:#1e9bd7}
</style>
</head>
<body>

<header class="site-header">
  <div class="brand"><span class="brand-dot"></span><span class="brand-name">Amber and Stone</span></div>
  <div class="call">
    <span class="call-icon"><svg width="16" height="16" viewBox="0 0 24 24"><path fill="#fff" d="M6.6 10.8c1.4 2.8 3.8 5.1 6.6 6.6l2.2-2.2c.3-.3.7-.4 1-.2 1.1.4 2.3.6 3.6.6.6 0 1 .4 1 1V20c0 .6-.4 1-1 1C10.6 21 3 13.4 3 4c0-.6.4-1 1-1h3.5c.6 0 1 .4 1 1 0 1.3.2 2.5.6 3.6.1.3 0 .7-.2 1z"/></svg></span>
    Call Now! <b>+34 600 218 457</b>
  </div>
  <div class="lang"><span class="lang-flag"></span><svg width="9" height="6" viewBox="0 0 9 6"><path d="M1 1l3.5 3.5L8 1" stroke="#333" fill="none" stroke-width="1.4"/></svg></div>
  <nav class="main-nav">
    <span class="active">Home</span><span>Experience</span><span>About Us</span><span>Contact Us</span><span class="btn-outline">Book Now</span>
  </nav>
</header>

<section class="hero">
  <div class="hero-photo" role="img" aria-label="Whitewashed Ibiza villa with balconies behind a large blue swimming pool, pines and sun loungers"></div>
  <h1 class="hero-title">The Best Way To Stay In Ibiza!</h1>
  <p class="hero-sub">More Than A Party Island ! Live The Real Experience of Ibiza!</p>
  <form class="search">
    <div class="search-labels">
      <span style="width:240px">Check-In And Check-Out Date</span>
      <span style="width:81px">Nights</span>
      <span style="width:177px">No. of Guests And Rooms</span>
      <span>Promo Code</span>
    </div>
    <div class="search-row">
      <div class="field" style="width:231px">Select dates for your stay
        <svg width="12" height="12" viewBox="0 0 12 12"><rect x="1" y="2" width="10" height="9" fill="none" stroke="#8fb14d"/><path d="M1 5h10" stroke="#8fb14d"/></svg></div>
      <div class="field" style="width:72px">1 <svg width="8" height="5" viewBox="0 0 8 5"><path d="M1 1l3 3 3-3" stroke="#8fb14d" fill="none"/></svg></div>
      <div class="field" style="width:168px">2 adults (1 room)
        <svg width="14" height="12" viewBox="0 0 14 12"><circle cx="4" cy="4" r="2.5" fill="#8fb14d"/><circle cx="10" cy="4" r="2.5" fill="#8fb14d"/><path d="M0 11c0-3 8-3 8 0zM6 11c0-3 8-3 8 0z" fill="#8fb14d"/></svg></div>
      <div class="field" style="width:140px">Promo
        <svg width="12" height="12" viewBox="0 0 12 12"><rect x="1" y="4" width="10" height="7" fill="#8fb14d"/><rect x="5" y="1" width="2" height="10" fill="#fff"/></svg></div>
      <div class="btn-search">SEARCH</div>
    </div>
  </form>
  <div class="dots"><i class="on"></i><i></i><i></i><i></i></div>
</section>

<section class="about">
  <div class="about-inner">
    <span class="rule"></span>
    <h2 class="section-title" style="margin-top:16px">About Amber and Stone</h2>
    <p class="about-sub">Villas Ibiza</p>
    <div class="about-copy">
      <p>Amber and Stone Villas Ibiza is a company <em>specialized in offering its clients accommodation in Villas on the countryside of Ibiza.</em> Our guests enjoy the rural Ibiza, tranquility, relax, private pool, close to dream beaches and coves, the best restaurants, an unforgettable holiday for family or friends.</p>
      <p>Every day can be a different experience, beach, restaurant, flea market, disco, hiking, kayaking, horseback riding, shopping, history, boat ride! There is a lot of variety for all budgets! The maximum distances of the island are 41 kilometers from north to south and 15 kilometers from east to west, we always recommend renting a car. Enjoy the freedom to go where you prefer, without depending on schedules or public transportation.</p>
    </div>
  </div>
  <div class="amenities">
    <div class="amenity"><div class="amenity-icon"><svg width="34" height="26" viewBox="0 0 34 26" fill="none" stroke="#444" stroke-width="2"><rect x="1" y="8" width="32" height="14" rx="2"/><path d="M8 3v3M13 3v3M18 3v3M23 3v3M6 17h22"/></svg></div>Aircondition<br>In Room</div>
    <div class="amenity"><div class="amenity-icon"><svg width="34" height="24" viewBox="0 0 34 24" fill="none" stroke="#444" stroke-width="2"><path d="M3 12l4-9h20l4 9v8H3z"/><circle cx="9" cy="15" r="2"/><circle cx="25" cy="15" r="2"/><path d="M5 20v3M29 20v3"/></svg></div>Rent A Car</div>
    <div class="amenity"><div class="amenity-icon"><svg width="30" height="30" viewBox="0 0 30 30" fill="none" stroke="#444" stroke-width="2"><path d="M4 12h22a11 9 0 0 1-22 0zM10 20l-4 9M20 20l4 9M15 3v6M10 5v4M20 5v4"/></svg></div>Barbecue</div>
    <div class="amenity"><div class="amenity-icon"><svg width="32" height="30" viewBox="0 0 32 30" fill="none" stroke="#444" stroke-width="2"><path d="M4 12a12 8 0 0 1 24 0zM16 12v16M6 24h20l-3-5H10z"/></svg></div>Sunbeds</div>
    <div class="amenity"><div class="amenity-icon"><svg width="26" height="30" viewBox="0 0 26 30" fill="none" stroke="#444" stroke-width="2"><rect x="1" y="1" width="24" height="28" rx="2"/><path d="M1 7h24"/><circle cx="13" cy="18" r="7"/></svg></div>Washing<br>Machine</div>
    <div class="amenity"><div class="amenity-icon"><svg width="32" height="28" viewBox="0 0 32 28" fill="none" stroke="#444" stroke-width="2"><path d="M8 20V3h5M20 20V3h5M8 9h12M8 15h12M1 22c4 3 6-3 10 0s6 3 10 0 6-3 10 0"/></svg></div>Outdoor<br>Swimming Pool</div>
    <div class="amenity"><div class="amenity-icon"><svg width="32" height="28" viewBox="0 0 32 28" fill="none" stroke="#444" stroke-width="2"><rect x="1" y="1" width="30" height="20"/><path d="M10 27h12M16 21v6M6 16l8-9 6 6 5-5"/></svg></div>Lounge<br>TV Area</div>
    <div class="amenity"><div class="amenity-icon"><svg width="30" height="24" viewBox="0 0 30 24" fill="none" stroke="#444" stroke-width="2"><path d="M2 8a19 19 0 0 1 26 0M6 12a13 13 0 0 1 18 0M10 16a7 7 0 0 1 10 0"/><circle cx="15" cy="21" r="1.5" fill="#444"/></svg></div>Free Wifi</div>
  </div>
  <a class="btn-pill read-more">READ MORE</a>
</section>

<section class="beaches">
  <div class="villa-slide" role="img" aria-label="Villa terrace with a private pool, white parasols, turquoise sunbeds and pine trees">
    <span class="villa-name">Villa Can Sera</span>
    <div class="slide-arrows">
      <span style="background:#fff"><svg width="10" height="16" viewBox="0 0 10 16"><path d="M8 1L2 8l6 7" stroke="#555" fill="none" stroke-width="1.6"/></svg></span>
      <span style="background:var(--green)"><svg width="10" height="16" viewBox="0 0 10 16"><path d="M2 1l6 7-6 7" stroke="#fff" fill="none" stroke-width="1.6"/></svg></span>
    </div>
  </div>
  <div class="beaches-text">
    <span class="rule left"></span>
    <h2>Ibiza's Beaches Are The Things</h2>
    <h3>That Dreams Are Made Of</h3>
    <p>Shimmering Crystalline Waters of Turquoise And Green And Fine White Sand In Gorgeous Coves</p>
    <a class="btn-pill contact-today">CONTACT US TODAY</a>
  </div>
</section>

<section class="video-banner" role="img" aria-label="Rustic villa interior with wooden doors, white walls, stone details and a cream sofa">
  <div class="shade"></div>
  <svg class="play" width="70" height="50" viewBox="0 0 70 50" fill="none" stroke="#fff" stroke-width="3"><rect x="2" y="2" width="66" height="42" rx="12"/><circle cx="35" cy="23" r="13"/><path d="M31 16l10 7-10 7z"/></svg>
  <h2 class="video-title">The Best Option To Stay In Ibiza</h2>
  <p class="video-sub">Lorem Ipsum Dolor Sit Consectetuer To Get Started!</p>
  <a class="btn-pill watch">WATCH A VIDEO</a>
</section>

<section class="gallery">
  <div class="head">
    <span class="rule"></span>
    <h2 class="section-title" style="margin-top:4px">Our Gallery</h2>
  </div>
  <div class="gallery-grid">
    <div class="tile t-pool" role="img" aria-label="Villa pool with palm trees under a blue sky"></div>
    <div class="tile t-beach" role="img" aria-label="Soft focus view of a sandy Ibiza beach and sea">
      <span class="expand"><svg width="36" height="36" viewBox="0 0 36 36" fill="none" stroke="#fff" stroke-width="2"><path d="M3 3l30 30M33 3L3 33M3 3h9M3 3v9M33 3h-9M33 3v9M3 33h9M3 33v-9M33 33h-9M33 33v-9"/></svg></span>
    </div>
    <div class="tile t-terrace" role="img" aria-label="Covered terrace with dining table overlooking the sea"></div>
    <div class="tile t-bedroom" role="img" aria-label="Bright bedroom with white linen"></div>
    <div class="tile t-bedroom2" role="img" aria-label="Whitewashed bedroom with wooden furniture"></div>
    <div class="tile t-lounge" role="img" aria-label="Living room with fireplace and sofas"></div>
    <div class="tile t-garden" role="img" aria-label="Garden pool with sunbeds and parasols among pines"></div>
  </div>
  <div class="view-all">View<br>All</div>
</section>

<section class="testimonials">
  <div class="head">
    <span class="rule"></span>
    <h2 class="section-title" style="margin-top:4px">Client Testimonials</h2>
  </div>
  <div class="avatar" role="img" aria-label="Guest portrait"></div>
  <p class="quote-name">- Marta</p>
  <span class="arrow-box arrow-prev"><svg width="10" height="16" viewBox="0 0 10 16"><path d="M8 1L2 8l6 7" stroke="#777" fill="none" stroke-width="1.6"/></svg></span>
  <span class="arrow-box arrow-next"><svg width="10" height="16" viewBox="0 0 10 16"><path d="M2 1l6 7-6 7" stroke="#fff" fill="none" stroke-width="1.6"/></svg></span>
  <span class="qmark" style="left:228px;top:360px">“</span>
  <p class="quote">Ruim opgezet huis met zwembad, veel badkamers en 5 slaapkamers. Meer dan voldoende bestek borden etc. helaas wel een bewoond appartementje onder het splitlevel huis waardoor je je toch niet helemaal 100%vrij voelde. Dit was niet beschreven. Top verhuurster en flxibel mbt komen en gaan.</p>
  <span class="qmark" style="left:888px;top:408px">”</span>
  <div class="t-dots"><i class="on"></i><i></i><i></i><i></i></div>
</section>

<section class="contact" role="img" aria-label="Ibiza old town on the hill above the harbour">
  <div class="shade"></div>
  <div class="head">
    <span class="rule light"></span>
    <h2 class="section-title" style="margin-top:4px">Contact Details</h2>
  </div>
  <div class="contact-items">
    <div class="c-item"><span class="c-icon"><svg width="14" height="18" viewBox="0 0 14 18"><path d="M7 0a7 7 0 0 1 7 7c0 5-7 11-7 11S0 12 0 7a7 7 0 0 1 7-7z" fill="#fff"/><circle cx="7" cy="7" r="2.5" fill="#2a4050"/></svg></span>
      <div>Carrer des Pinar,<br>8, Sant Josep,<br>07830, Ibiza</div></div>
    <div class="c-item"><span class="c-icon"><svg width="16" height="16" viewBox="0 0 24 24"><path fill="#fff" d="M6.6 10.8c1.4 2.8 3.8 5.1 6.6 6.6l2.2-2.2c.3-.3.7-.4 1-.2 1.1.4 2.3.6 3.6.6.6 0 1 .4 1 1V20c0 .6-.4 1-1 1C10.6 21 3 13.4 3 4c0-.6.4-1 1-1h3.5c.6 0 1 .4 1 1 0 1.3.2 2.5.6 3.6.1.3 0 .7-.2 1z"/></svg></span>
      <div><div class="label">Call Us</div><div class="val">+34 600 218 457</div></div></div>
    <div class="c-item"><span class="c-icon"><svg width="16" height="12" viewBox="0 0 16 12"><rect width="16" height="12" rx="1" fill="#fff"/><path d="M1 1l7 6 7-6" stroke="#2a4050" fill="none" stroke-width="1.4"/></svg></span>
      <div><div class="label">Email Us</div><div class="val">reservas@amberandstonevillas.example</div></div></div>
  </div>
</section>

<footer class="site-footer">
  <div class="brand"><span class="brand-dot"></span><span class="brand-name">Amber and Stone</span></div>
  <nav class="foot-nav"><span>Home</span><span>Experience</span><span>About Us</span><span>Contact Us</span></nav>
  <p class="copyright">Copyright © 2019 Amber and Stone Villas Ibiza. All Rights Reserved.</p>
  <div class="social"><i class="a"></i><i class="b"></i></div>
</footer>

</body>
</html>
```